Physiotherapy business needs patient information graphic redesign

We have existing graphics that we need redesigned to add some artistic flare. The images must remain professional and suitable for a healthcare setting but some artistic flare is need to add interest to the graphics so that patients are able to engage more easily with the info sheet. Graphics include "INS", "graded activity", "pacing I", "pacing II" and "sleep"

Target Market(s)

Practitioners and patients with pain

Industry/Entity Type

Business

Font styles to use
Sans Serif

Colors
3176b5
9bcb3b
ec1f27

Requirements
Must have
• The ability to communicate the message in the graphic
• Artistic flair
• Retain professionalism
Nice to have
• Unique creativity that distinguishes our product
• Matching with our logo (attached). Does not have to be the same colours or style/font but still should fit with the logo stylistically
Should not have
• A similar boring and flat feel as the existing graphics

```html
<!DOCTYPE html>
<html lang="en">
<head>
<meta charset="utf-8">
<title>Pacing – Boom and Bust Cycle</title>
<link rel="stylesheet" href="https://fonts.googleapis.com/css2?family=Source+Sans+3:wght@400;500&display=swap">
<style>
  :root {
    --teal: #5dd9d1;
    --teal-deep: #1fbcb0;
    --teal-light: #8ff7ee;
    --red: #e73b35;
    --red-deep: #b81f2a;
    --red-text: #e8174a;
    --disc: #f4f4f4;
    --disc-shade: #e2e2e2;
    --bg: #ffffff;
  }
  html, body {
    margin: 0;
    padding: 0;
    width: 1200px;
    height: 1200px;
    overflow: hidden;
    background: var(--bg);
  }
  .pacing-chart {
    display: block;
    width: 1200px;
    height: 1200px;
    font-family: "Source Sans 3", sans-serif;
  }
  .axis, .activity-line {
    fill: none;
    stroke: var(--teal);
    stroke-linecap: round;
    stroke-linejoin: miter;
  }
  .axis { stroke-width: 8; }
  .activity-line { stroke-width: 5; }
  .axis-marker { fill: var(--bg); stroke: var(--teal); stroke-width: 4; }
  .axis-label {
    fill: var(--teal);
    font-size: 27px;
    font-weight: 400;
    text-anchor: end;
  }
  .overdo-label {
    fill: var(--red-text);
    font-size: 16.5px;
    text-anchor: middle;
  }
  .rest-label {
    fill: var(--teal);
    font-size: 27px;
    font-weight: 500;
    text-anchor: middle;
  }
</style>
</head>
<body>
<svg class="pacing-chart" viewBox="0 0 1500 1500" xmlns="http://www.w3.org/2000/svg">
  <defs>
    <linearGradient id="ring-red" x1="0" y1="0" x2="0" y2="1">
      <stop offset="0" stop-color="var(--red)"/>
      <stop offset="1" stop-color="var(--red-deep)"/>
    </linearGradient>
    <linearGradient id="wedge-teal" x1="0" y1="0" x2="1" y2="1">
      <stop offset="0" stop-color="var(--teal-light)"/>
      <stop offset="1" stop-color="var(--teal-deep)"/>
    </linearGradient>
    <radialGradient id="disc-grey" cx="0.4" cy="0.35" r="0.75">
      <stop offset="0" stop-color="#fbfbfb"/>
      <stop offset="1" stop-color="var(--disc-shade)"/>
    </radialGradient>
    <filter id="soft-shadow" x="-40%" y="-40%" width="180%" height="180%">
      <feDropShadow dx="0" dy="10" stdDeviation="9" flood-color="#000" flood-opacity="0.2"/>
    </filter>
    <filter id="inner-shadow" x="-40%" y="-40%" width="180%" height="180%">
      <feDropShadow dx="0" dy="8" stdDeviation="6" flood-color="#000" flood-opacity="0.25"/>
    </filter>
  </defs>

  <!-- axes -->
  <path class="axis" d="M229 515 V1032 H1408"/>
  <circle class="axis-marker" cx="229" cy="638" r="14"/>
  <circle class="axis-marker" cx="229" cy="918" r="14"/>

  <text class="axis-label" x="193" y="630">NORMAL</text>
  <text class="axis-label" x="193" y="662">ACTIVITY</text>
  <text class="axis-label" x="182" y="915">UNDER</text>
  <text class="axis-label" x="193" y="947">ACTIVITY</text>

  <!-- activity trace -->
  <polyline class="activity-line" points="275,916 407,916 469,732 533,916 600,916"/>
  <polyline class="activity-line" points="680,916 743,916 805,732 868,916 935,916"/>
  <polyline class="activity-line" points="1015,916 1078,916 1140,732 1204,916 1336,916"/>

  <!-- overdo activity peaks -->
  <g class="overdo-node" transform="translate(469 654)">
    <circle r="77" fill="url(#ring-red)" filter="url(#soft-shadow)"/>
    <path d="M0 -77 A77 77 0 0 0 -70.9 -30.1 L-46 -19.5 A50 50 0 0 1 0 -50 Z" fill="#fafafa"/>
    <circle r="50" fill="url(#disc-grey)" filter="url(#inner-shadow)"/>
    <text class="overdo-label" y="-4">OVERDO</text>
    <text class="overdo-label" y="18">ACTIVITY</text>
  </g>
  <g class="overdo-node" transform="translate(806 654)">
    <circle r="77" fill="url(#ring-red)" filter="url(#soft-shadow)"/>
    <path d="M0 -77 A77 77 0 0 0 -70.9 -30.1 L-46 -19.5 A50 50 0 0 1 0 -50 Z" fill="#fafafa"/>
    <circle r="50" fill="url(#disc-grey)" filter="url(#inner-shadow)"/>
    <text class="overdo-label" y="-4">OVERDO</text>
    <text class="overdo-label" y="18">ACTIVITY</text>
  </g>
  <g class="overdo-node" transform="translate(1140 654)">
    <circle r="77" fill="url(#ring-red)" filter="url(#soft-shadow)"/>
    <path d="M0 -77 A77 77 0 0 0 -70.9 -30.1 L-46 -19.5 A50 50 0 0 1 0 -50 Z" fill="#fafafa"/>
    <circle r="50" fill="url(#disc-grey)" filter="url(#inner-shadow)"/>
    <text class="overdo-label" y="-4">OVERDO</text>
    <text class="overdo-label" y="18">ACTIVITY</text>
  </g>

  <!-- rest troughs -->
  <g class="rest-node" transform="translate(639 921)">
    <circle r="77" fill="var(--disc)" filter="url(#soft-shadow)"/>
    <path d="M0 -77 A77 77 0 0 1 69.8 -32.5 L44.4 -20.7 A49 49 0 0 0 0 -49 Z" fill="url(#wedge-teal)"/>
    <circle r="49" fill="url(#disc-grey)" filter="url(#inner-shadow)"/>
    <text class="rest-label" y="9">REST</text>
  </g>
  <g class="rest-node" transform="translate(973 921)">
    <circle r="77" fill="var(--disc)" filter="url(#soft-shadow)"/>
    <path d="M0 -77 A77 77 0 0 1 69.8 -32.5 L44.4 -20.7 A49 49 0 0 0 0 -49 Z" fill="url(#wedge-teal)"/>
    <circle r="49" fill="url(#disc-grey)" filter="url(#inner-shadow)"/>
    <text class="rest-label" y="9">REST</text>
  </g>
</svg>
</body>
</html>
```